Painting Company Business Card

Brightwell Painting needs a new business card. See attachments for our logo and current card as an example.
We want to utilize the same colors in the logo, and keep all the information that is currently on it. Just need an updated and modern design.
We are open to loosing the Association Logos if it means a better design.
We are also entertaining a spot for a picture of a headshot of the person listed on the card. Head shot can be finished later.

```html
<!DOCTYPE html>
<html lang="en">
<head>
<meta charset="utf-8">
<title>Brightwell Painting – Business Card</title>
<link href="https://fonts.googleapis.com/css2?family=Montserrat:wght@400;500;700&display=swap" rel="stylesheet">
<style>
  :root {
    --backdrop: #3a3330;
    --maroon: #6b3330;
    --maroon-text: #6e2f2c;
    --forest: #4b5a3c;
    --forest-text: #3f4d31;
    --paper: #ffffff;
    --ink: #3a3a3a;
  }
  * { margin: 0; padding: 0; box-sizing: border-box; }
  html, body { width: 1200px; height: 716px; overflow: hidden; }
  body {
    background: var(--backdrop);
    font-family: "Montserrat", sans-serif;
    position: relative;
  }
  .card {
    position: absolute;
    top: 210px;
    width: 520px;
    height: 297px;
    border-radius: 4px;
    overflow: hidden;
  }

  /* Front */
  .card-front {
    left: 50px;
    background: var(--maroon);
    color: var(--paper);
  }
  .front-brand {
    position: absolute;
    left: 0; right: 0;
    top: 82px;
    display: flex;
    align-items: center;
    justify-content: center;
    gap: 14px;
  }
  .brand-square {
    width: 22px; height: 22px;
    background: var(--paper);
  }
  .brand-name {
    font-weight: 700;
    font-size: 34px;
    line-height: 1.05;
    letter-spacing: 0.5px;
  }
  .services {
    position: absolute;
    left: 0; right: 0;
    bottom: 40px;
    display: flex;
    justify-content: center;
    gap: 18px;
    font-size: 13px;
    font-weight: 500;
    list-style: none;
  }
  .services li::before {
    content: "";
    display: inline-block;
    width: 6px; height: 6px;
    border-radius: 50%;
    background: var(--paper);
    margin-right: 5px;
    vertical-align: middle;
  }

  /* Back */
  .card-back {
    left: 630px;
    background: var(--paper);
  }
  .back-brand {
    position: absolute;
    left: 28px;
    top: 92px;
    width: 190px;
    display: flex;
    align-items: center;
    gap: 10px;
    color: var(--forest-text);
  }
  .back-brand .brand-square { background: var(--forest); width: 18px; height: 18px; flex: none; }
  .back-brand .brand-name { font-size: 25px; }
  .divider {
    position: absolute;
    left: 232px;
    top: 48px;
    width: 1px;
    height: 170px;
    background: var(--maroon);
  }
  .contact {
    position: absolute;
    left: 252px;
    top: 52px;
    color: var(--ink);
  }
  .person-name {
    font-size: 21px;
    font-weight: 700;
    color: var(--forest-text);
  }
  .person-role {
    font-size: 14px;
    font-weight: 500;
    color: var(--maroon-text);
    margin-bottom: 12px;
  }
  .company {
    font-size: 12.5px;
    font-weight: 700;
    color: var(--ink);
  }
  .address {
    font-size: 12.5px;
    line-height: 1.4;
    margin-bottom: 8px;
    font-style: normal;
  }
  .contact-line {
    display: flex;
    align-items: center;
    gap: 6px;
    font-size: 12.5px;
    line-height: 1.55;
  }
  .contact-line svg { width: 12px; height: 12px; flex: none; }
  .web-name { color: var(--maroon-text); font-weight: 700; }
  .band {
    position: absolute;
    left: 0; right: 0; bottom: 0;
    height: 16px;
    display: flex;
  }
  .band-forest { width: 38%; background: var(--forest); }
  .band-maroon { flex: 1; background: var(--maroon); margin-left: 3px; }
</style>
</head>
<body>

<section class="card card-front">
  <div class="front-brand">
    <span class="brand-square"></span>
    <span class="brand-name">Brightwell<br>Painting</span>
  </div>
  <ul class="services">
    <li>Exterior Painting</li>
    <li>Interior Painting</li>
    <li>Carpentry</li>
    <li>Drywall</li>
  </ul>
</section>

<section class="card card-back">
  <div class="back-brand">
    <span class="brand-square"></span>
    <span class="brand-name">Brightwell<br>Painting</span>
  </div>
  <div class="divider"></div>
  <div class="contact">
    <div class="person-name">Daniel Hartley</div>
    <div class="person-role">Quality Manager</div>
    <div class="company">Brightwell Painting, LLC</div>
    <address class="address">Office: 480 Cedar Lane #2<br>Riverton, WI 53100</address>
    <div class="contact-line">
      <svg viewBox="0 0 24 24" fill="#3a3a3a"><path d="M6.6 10.8a15.1 15.1 0 0 0 6.6 6.6l2.2-2.2c.3-.3.7-.4 1-.2 1.1.4 2.3.6 3.6.6.6 0 1 .4 1 1V20c0 .6-.4 1-1 1A17 17 0 0 1 3 4c0-.6.4-1 1-1h3.5c.6 0 1 .4 1 1 0 1.3.2 2.5.6 3.6.1.3 0 .7-.2 1z"/></svg>
      <span>262-555-0148</span>
    </div>
    <div class="contact-line">
      <svg viewBox="0 0 24 24" fill="none" stroke="#3a3a3a" stroke-width="2"><rect x="3" y="5" width="18" height="14" rx="1"/><path d="M3 6l9 7 9-7"/></svg>
      <span>daniel@brightwellmail.com</span>
    </div>
    <div class="contact-line">
      <svg viewBox="0 0 24 24" fill="none" stroke="#3a3a3a" stroke-width="2"><circle cx="12" cy="12" r="9"/><path d="M3 12h18M12 3c3 3 3 15 0 18M12 3c-3 3-3 15 0 18"/></svg>
      <span>www.<span class="web-name">brightwellpainting</span>.com</span>
    </div>
  </div>
  <div class="band"><span class="band-forest"></span><span class="band-maroon"></span></div>
</section>

</body>
</html>
```